E-learning Information & Community Website Needs a Makeover

I'm looking for a design makeover for my website "Vetrola.club". Vetrola's aim is to connect people to online learning through forums, information, guides & independent reviews. The site was launched in September 2014 using a forum software (Xenforo), but now needs a more polished and sophisticated look which communicates expertise and professionalism. I would like to see designs that use the current "Vetrola" blue (#0070c0). To visit the current website, go to http://www.vetrola.club/

Target Market(s)

People wishing to study online

Industry/Entity Type

Club

Number of Pages Required

4 page

Font styles to use
Sans Serif

Requirements
Must have
• A simple, clear and sophisticated lading page with links to the site's key features: discussion forums, Useful resources, Reviews, News etc, Articles. (See layout idea file attached)
• The main pages are the Landing Page, Discussion Forums, Resources & Reviews
• I would like to see designs that use the current "Vetrola" blue (#0070c0).
Nice to have
• Something uncluttered and easy to understand. The design should convey expertise in the field of online learning, giving users a sense of trust in the site's offerings.
• To give an idea of the sort of thing I'm after, take a look at brantivo.com website (screenshot attached)

```html
<!DOCTYPE html>
<html lang="en">
<head>
<meta charset="utf-8">
<title>Vetrola – Connecting people to online learning</title>
<link href="https://fonts.googleapis.com/css2?family=Cabin:ital,wght@0,400;0,500;0,600;1,400&family=Lato:wght@400;700&family=Dancing+Script:wght@600&display=swap" rel="stylesheet">
<style>
:root{
  --brand:#0070c0;
  --hero-a:#1d86d6;
  --hero-b:#0a62b8;
  --header:#333333;
  --ink:#444;
  --muted:#888;
  --green-a:#9ad33b;
  --green-b:#5fae1a;
  --tile-green:#9ad13c;
  --tile-orange:#f47c54;
  --tile-purple:#8a72b0;
  --tile-red:#e4506d;
  --tile-sky:#5bbad8;
  --tile-yellow:#f4c542;
  --band-grey:#ececec;
  --foot-bg:#e6f2f3;
  --side-bg:#e9ecef;
  --line:#dadada;
}
*{box-sizing:border-box;margin:0;padding:0}
html,body{width:1027px;height:1200px;overflow:hidden}
body{position:relative;background:#fff;font-family:"Cabin",sans-serif;color:var(--ink)}
.abs{position:absolute}
a{color:inherit;text-decoration:none}

/* header */
.site-header{left:0;top:0;width:1027px;height:47px;background:var(--header)}
.brand-name{left:138px;top:8px;font-size:24px;color:#9fd2f5}
.nav-link{top:15px;font-size:12.5px;color:#fff;white-space:nowrap}
.account{left:801px;top:15px;font-size:12.5px;color:#9fd2f5}
.btn-signup-sm{left:846px;top:11px;width:53px;height:24px;border-radius:4px;background:var(--brand);color:#fff;font-size:12.5px;text-align:center;line-height:24px}

/* hero */
.hero{left:0;top:47px;width:1027px;height:381px;background:linear-gradient(180deg,var(--hero-a),var(--hero-b))}
.hero-kicker{left:137px;top:134px;font-size:25px;color:#8fd4ff}
.hero-title{left:137px;top:162px;font-size:42px;line-height:50px;color:#fff;font-weight:400}
.btn-green{background:linear-gradient(180deg,var(--green-a),var(--green-b));color:#fff;border-radius:17px;text-align:center;font-size:17px}
.hero-cta{left:136px;top:280px;width:187px;height:34px;line-height:34px}
.hero-art{left:508px;top:100px;width:450px;height:290px;border-radius:20px;background:radial-gradient(ellipse at center,rgba(255,255,255,.22),rgba(255,255,255,.04) 70%)}
.hero-share{left:832px;top:75px;display:flex;gap:4px}
.dot{width:11px;height:11px;border-radius:50%;background:#fff}

/* tiles */
.tile{top:405px;width:85px;height:85px;display:flex;align-items:center;justify-content:center}
.tile-label{top:498px;width:120px;text-align:center;font-size:12px;color:#555}
.share-title{left:751px;top:433px;font-family:"Dancing Script",cursive;color:var(--brand);font-size:12px}
.share-btn{font-family:"Lato",sans-serif;font-size:8px;border:1px solid #ccc;height:13px;line-height:11px;padding:0 3px;color:#333;background:#fff}
.share-btn.solid{background:var(--brand);color:#fff;border-color:var(--brand)}

/* partners */
.partners-band{left:0;top:540px;width:1027px;height:104px;background:var(--band-grey)}
.partners{left:136px;top:560px;width:760px;height:65px;background:#fff;box-shadow:0 1px 2px rgba(0,0,0,.1);display:flex;align-items:center;justify-content:space-around;padding:0 55px;color:#9a9a9a;font-size:15px}
.partner{display:flex;align-items:center;gap:5px;font-family:"Lato",sans-serif}
.partner i{display:inline-block;width:14px;height:14px;background:#bbb;border-radius:50%}
.arrow-nav{top:582px;color:#ccc;font-size:20px}

/* threads */
.threads-head{top:656px;font-size:13px;color:var(--brand)}
.col-head{top:657px;font-size:12px;color:var(--brand)}
.thread-line{left:138px;width:552px;height:1px;background:var(--line)}
.avatar{width:52px;height:52px;border-radius:50%;background:var(--brand);color:#fff;font-size:10px;text-align:center;line-height:12px;padding-top:15px}
.tag{width:32px;height:10px;font-size:7px;line-height:10px;text-align:center;color:#fff}
.thread-title{font-size:13px;color:var(--brand)}
.thread-meta{font-size:10px;color:var(--muted)}
.reply{width:40px;height:28px;background:var(--brand);color:#fff;font-size:12px;text-align:center;line-height:28px}
.last-msg{font-size:10px;color:var(--muted);line-height:11px}
.last-msg b{color:var(--brand);font-weight:400}
.more{left:444px;top:984px;width:148px;height:23px;border-radius:74px 74px 0 0;background:var(--brand);color:#fff;font-size:12px;text-align:center;padding-top:7px;line-height:14px}

/* sidebar */
.feed{left:708px;top:652px;width:188px;height:198px;background:var(--side-bg)}
.feed-title{left:747px;top:666px;font-size:13px;color:var(--brand)}
.feed-bird{left:718px;top:661px;width:24px;height:24px;border-radius:50%;background:#3fa0e0}
.feed-list{left:714px;top:694px;width:176px;height:150px;background:#fff;font-family:"Lato",sans-serif;font-size:7.5px;color:#333;overflow:hidden}
.post{position:relative;height:42px;border-bottom:1px solid #eee;padding:4px 4px 0 34px;line-height:9.5px}
.post.first{height:62px}
.post i{position:absolute;left:4px;top:6px;width:25px;height:25px;background:var(--brand)}
.post em{font-style:normal;color:#aaa}
.post span{color:var(--brand)}
.follow{left:708px;top:860px;width:188px;height:90px;background:var(--side-bg)}
.follow-title{left:720px;top:871px;font-size:13px;color:var(--brand)}
.social{top:895px;width:30px;height:30px}

/* footer */
.footer-band{left:0;top:1007px;width:1027px;height:193px;background:var(--foot-bg)}
.footer-tag{left:0;top:1034px;width:1027px;text-align:center;font-style:italic;font-size:18px;color:var(--brand)}
.footer-cta{left:423px;top:1064px;width:186px;height:33px;line-height:33px}
.footer-links{left:249px;top:1110px;width:532px;height:47px;background:#f7fbfb;font-size:11px;color:var(--brand);display:flex;align-items:center;padding-left:35px;gap:15px}
.to-top{left:724px;top:1125px;font-size:10px;color:#555;display:flex;align-items:center;gap:6px}
.copy{left:282px;top:1172px;font-family:"Lato",sans-serif;font-size:8px;color:#777}
.foot-share{left:528px;top:1172px;display:flex;gap:3px}
.foot-share i{width:13px;height:13px;border-radius:50%;background:var(--brand)}
.foot-share i:last-child{background:#e0553f}
.legal{left:666px;top:1172px;font-family:"Lato",sans-serif;font-size:8px;color:var(--brand)}
</style>
</head>
<body>

<header class="site-header abs">
  <div class="brand-name abs">Vetrola</div>
  <nav>
    <a class="nav-link abs" style="left:276px" href="#">Home</a>
    <a class="nav-link abs" style="left:323px" href="#">Forums</a>
    <a class="nav-link abs" style="left:379px" href="#">Resources</a>
    <a class="nav-link abs" style="left:449px" href="#">Members</a>
    <a class="nav-link abs" style="left:516px" href="#">FAQ</a>
    <a class="nav-link abs" style="left:552px" href="#">Blog</a>
    <a class="nav-link abs" style="left:591px" href="#">Vetrola Español</a>
    <a class="nav-link abs" style="left:702px" href="#">Vetrola Scoop</a>
  </nav>
  <div class="account abs">Login &nbsp;|</div>
  <a class="btn-signup-sm abs" href="#">Signup</a>
</header>

<section class="hero abs">
  <div class="hero-share abs" style="top:28px"><i class="dot"></i><i class="dot"></i><i class="dot"></i><i class="dot"></i></div>
</section>
<div class="hero-art abs" role="img" aria-label="Illustration of online learning: a teacher at a board with students, a graduation cap, devices, a gear and signposts circling the Vetrola name"></div>
<div class="hero-kicker abs">At the heart of</div>
<h1 class="hero-title abs">connecting people to<br>online learning</h1>
<a class="btn-green hero-cta abs" href="#">Sign Up For Free</a>

<a class="tile abs" style="left:136px;background:var(--tile-green)" href="#">
  <svg width="40" height="40" viewBox="0 0 40 40"><circle cx="20" cy="20" r="17" fill="none" stroke="#fff" stroke-width="3"/><path d="M16 12 L28 20 L16 28Z" fill="#fff"/></svg>
</a>
<a class="tile abs" style="left:238px;background:var(--tile-orange)" href="#">
  <svg width="40" height="36" viewBox="0 0 40 36"><path d="M2 2H38V26H14L6 33V26H2Z" fill="#fff"/><g stroke="var(--tile-orange)" stroke-width="2"><line x1="9" y1="9" x2="31" y2="9"/><line x1="9" y1="14" x2="31" y2="14"/><line x1="9" y1="19" x2="31" y2="19"/></g></svg>
</a>
<a class="tile abs" style="left:341px;background:var(--tile-purple)" href="#">
  <svg width="40" height="38" viewBox="0 0 40 38"><path d="M4 2H36V28H16L8 35V28H4Z" fill="#fff"/><circle cx="20" cy="15" r="9" fill="var(--tile-purple)"/><path d="M15 15l4 4 6-7" fill="none" stroke="#fff" stroke-width="2.5"/></svg>
</a>
<a class="tile abs" style="left:443px;background:var(--tile-red)" href="#">
  <svg width="30" height="42" viewBox="0 0 30 42"><path d="M15 3a11 11 0 0 0-6 20v6h12v-6a11 11 0 0 0-6-20z" fill="none" stroke="#fff" stroke-width="2.5"/><rect x="9" y="32" width="12" height="3" fill="#fff"/><rect x="11" y="37" width="8" height="3" fill="#fff"/></svg>
</a>
<a class="tile abs" style="left:546px;background:var(--tile-sky)" href="#">
  <svg width="34" height="42" viewBox="0 0 34 42"><path d="M2 2H24L32 10V40H2Z" fill="#fff"/><g stroke="var(--tile-sky)" stroke-width="1.5"><line x1="7" y1="18" x2="27" y2="18"/><line x1="7" y1="23" x2="27" y2="23"/><line x1="7" y1="28" x2="27" y2="28"/><line x1="7" y1="33" x2="27" y2="33"/></g></svg>
</a>
<a class="tile abs" style="left:650px;background:var(--tile-yellow)" href="#">
  <svg width="42" height="30" viewBox="0 0 42 30"><rect x="1" y="1" width="40" height="28" fill="#fff8e0" stroke="#fff" stroke-width="2"/><path d="M1 1L21 17L41 1" fill="none" stroke="#e8b42c" stroke-width="1.5"/></svg>
</a>
<div class="tile-label abs" style="left:118px">Getting Started</div>
<div class="tile-label abs" style="left:220px">Discussions</div>
<div class="tile-label abs" style="left:323px">Reviews</div>
<div class="tile-label abs" style="left:425px">Tips &amp; Guidelines</div>
<div class="tile-label abs" style="left:528px">News &amp; Articles</div>
<div class="tile-label abs" style="left:632px">Newsletter</div>

<div class="share-title abs">Share This Page</div>
<span class="share-btn abs" style="left:751px;top:455px">Post</span>
<span class="share-btn abs" style="left:789px;top:455px">139</span>
<span class="share-btn abs" style="left:834px;top:455px">+1</span>
<span class="share-btn abs" style="left:858px;top:455px">21</span>
<span class="share-btn solid abs" style="left:751px;top:473px">Like</span>
<span class="share-btn abs" style="left:808px;top:473px">157</span>
<span class="share-btn solid abs" style="left:834px;top:473px">Share</span>
<span class="share-btn abs" style="left:878px;top:473px">43</span>

<div class="partners-band abs"></div>
<div class="partners abs">
  <div class="partner"><i></i>Fernwick</div>
  <div class="partner"><i></i>Oaklight</div>
  <div class="partner"><i style="width:28px;height:28px"></i>Tidemark</div>
  <div class="partner">Halvern</div>
  <div class="partner"><i></i>Brightmoor</div>
  <div class="partner"><i style="border-radius:2px"></i>Quillstone</div>
</div>
<div class="arrow-nav abs" style="left:140px">‹</div>
<div class="arrow-nav abs" style="left:880px">›</div>

<div class="threads-head abs" style="left:141px">Recent Threads</div>
<div class="col-head abs" style="left:470px">Replies</div>
<div class="col-head abs" style="left:534px">Views</div>
<div class="col-head abs" style="left:607px">Last Message</div>
<div class="thread-line abs" style="top:679px"></div>

<div class="avatar abs" style="left:139px;top:686px">Vetrola</div>
<div class="tag abs" style="left:149px;top:725px;background:#7cc242">Advice</div>
<div class="thread-title abs" style="left:209px;top:696px">How many MOOCs have you done?</div>
<div class="thread-meta abs" style="left:209px;top:714px">Marissa, Sep 19, 2014, MOOC Discussions</div>
<div class="reply abs" style="left:469px;top:690px">01</div>
<svg class="abs" style="left:528px;top:692px" width="44" height="26" viewBox="0 0 44 26"><path d="M1 13Q22 -6 43 13Q22 32 1 13Z" fill="var(--brand)"/><circle cx="22" cy="13" r="9" fill="#fff"/><text x="22" y="17" font-size="10" text-anchor="middle" fill="var(--brand)" font-family="Cabin,sans-serif">36</text></svg>
<div class="last-msg abs" style="left:605px;top:692px"><b>Marissa,</b><br>Yesterday at 4:41 PM</div>
<div class="thread-line abs" style="top:751px"></div>

<div class="avatar abs" style="left:139px;top:757px">Vetrola</div>
<div class="tag abs" style="left:149px;top:796px;background:#7cc242">Advice</div>
<div class="thread-title abs" style="left:209px;top:767px">How many MOOCs have you done?</div>
<div class="thread-meta abs" style="left:209px;top:785px">Marissa, Sep 19, 2014, MOOC Discussions</div>
<div class="reply abs" style="left:469px;top:762px">01</div>
<svg class="abs" style="left:528px;top:763px" width="44" height="26" viewBox="0 0 44 26"><path d="M1 13Q22 -6 43 13Q22 32 1 13Z" fill="var(--brand)"/><circle cx="22" cy="13" r="9" fill="#fff"/><text x="22" y="17" font-size="10" text-anchor="middle" fill="var(--brand)" font-family="Cabin,sans-serif">36</text></svg>
<div class="last-msg abs" style="left:605px;top:763px"><b>Marissa,</b><br>Yesterday at 4:41 PM</div>
<div class="thread-line abs" style="top:822px"></div>

<div class="avatar abs" style="left:139px;top:831px">Vetrola</div>
<div class="tag abs" style="left:149px;top:870px;background:#f07d3a">Courses</div>
<div class="thread-title abs" style="left:209px;top:841px">How many MOOCs have you done?</div>
<div class="thread-meta abs" style="left:209px;top:859px">Marissa, Sep 19, 2014, MOOC Discussions</div>
<div class="reply abs" style="left:469px;top:835px">01</div>
<svg class="abs" style="left:528px;top:837px" width="44" height="26" viewBox="0 0 44 26"><path d="M1 13Q22 -6 43 13Q22 32 1 13Z" fill="var(--brand)"/><circle cx="22" cy="13" r="9" fill="#fff"/><text x="22" y="17" font-size="10" text-anchor="middle" fill="var(--brand)" font-family="Cabin,sans-serif">36</text></svg>
<div class="last-msg abs" style="left:605px;top:836px"><b>Marissa,</b><br>Yesterday at 4:41 PM</div>
<div class="thread-line abs" style="top:895px"></div>

<div class="avatar abs" style="left:139px;top:908px">Vetrola</div>
<div class="tag abs" style="left:149px;top:947px;background:#7cc242">Advice</div>
<div class="thread-title abs" style="left:209px;top:917px">How many MOOCs have you done?</div>
<div class="thread-meta abs" style="left:209px;top:936px">Marissa, Sep 19, 2014, MOOC Discussions</div>
<div class="reply abs" style="left:469px;top:912px">01</div>
<svg class="abs" style="left:528px;top:913px" width="44" height="26" viewBox="0 0 44 26"><path d="M1 13Q22 -6 43 13Q22 32 1 13Z" fill="var(--brand)"/><circle cx="22" cy="13" r="9" fill="#fff"/><text x="22" y="17" font-size="10" text-anchor="middle" fill="var(--brand)" font-family="Cabin,sans-serif">36</text></svg>
<div class="last-msg abs" style="left:605px;top:913px"><b>Marissa,</b><br>Yesterday at 4:41 PM</div>

<div class="feed abs"></div>
<div class="feed-bird abs"></div>
<div class="feed-title abs">Chirpline Feeds</div>
<div class="feed-list abs">
  <div class="post first"><i></i><b>Nimbusworks</b> <em>8/23/13</em><br>@danvarel is back with a blogpost on #API Interactions with #KVO in #ObjectiveC! · <span>nmbw.io/k72tq</span><br><em>Promoted by Nimbusworks</em></div>
  <div class="post"><i style="background:#fff;border:1px solid #1c4f7a"></i><b>Daily Ledger Politics</b> <em>51s</em><br>Here's why shady for-profit colleges won't get shut down <span>ldgr.io/p8qv</span></div>
  <div class="post" style="border:0"><i style="background:#2a6f8e"></i><b>DT: Tech</b> <em>@DTtech 1m</em><br>New Yorkers may be more superficial than people in LA when it comes to dating <span>dtnw.io/c7pw</span></div>
</div>
<div class="follow abs"></div>
<div class="follow-title abs">FOLLOW US</div>
<div class="social abs" style="left:721px;background:#3b5998"></div>
<div class="social abs" style="left:752px;background:#2ea3e3"></div>
<div class="social abs" style="left:784px;background:#fff"></div>
<div class="social abs" style="left:815px;background:#111"></div>
<div class="social abs" style="left:847px;background:#27a7d8"></div>

<footer>
  <div class="footer-band abs"></div>
  <a class="more abs" href="#">⌄ more activities</a>
  <div class="footer-tag abs">At the heart of connecting people to online learning</div>
  <a class="btn-green footer-cta abs" href="#">Sign Up For Free</a>
  <nav class="footer-links abs"><a href="#">About</a><a href="#">Contact Us</a><a href="#">Help</a><a href="#">Home</a><a href="#">FAQ</a><a href="#">Community Guidelines</a></nav>
  <div class="to-top abs"><svg width="15" height="15" viewBox="0 0 15 15"><circle cx="7.5" cy="7.5" r="7.5" fill="var(--brand)"/><path d="M4.5 9L7.5 6L10.5 9" fill="none" stroke="#fff" stroke-width="1.6"/></svg>Top</div>
  <div class="copy abs">All Rights Reserved ™ ©2010-2015 Vetrola.</div>
  <div class="foot-share abs"><i></i><i></i><i></i><i></i></div>
  <div class="legal abs">Terms and Rules &nbsp;&nbsp; Forum</div>
</footer>

</body>
</html>
```